Einfache Webside für kleine Promotion- und Personalagentur
Zielgruppe
Lumo Staffing ist eine international tätige Promotion- und Personalagentur. Wir bieten auch im Bereich Sport der jew. Sportart affine Hostessen und Hosts f an.
Aufgabenstellung
Wir hatten bis dato eine sehr gute Auftragslage und leider keine Zeit für eine Homepage. Wir suchen jemaden der uns das Design für die Seite übernimmt und Online stellt. Wir sind auch offen wenn dies über z.B. Q+Z erfolgt. Auf den jeweiligen Seiten wollen wir den Text dann immer selbst eintragen. Seiten: Startseite mit Buttons zu folgenden Feldern: Promotion (Text mit Erklärung was wir machen und Bildern), Personal (Text mit Erklärung was wir machen und Bilder - die Bilder sollten austauschbar sein), Team, Referenzen, Kontaktseite, Gästebuch, Impressum. Die Seite sollte Modern aussehen und nicht zu überladen sein.

```html
<!DOCTYPE html>
<html lang="de">
<head>
<meta charset="utf-8">
<title>Lumo Staffing – Promotion</title>
<link href="https://fonts.googleapis.com/css2?family=Source+Sans+3:wght@400;600;700&display=swap" rel="stylesheet">
<style>
:root{
  --cyan:#7ecbd8;
  --slate:#8a939c;
  --slate-line:#7d868f;
  --mist:#ebedef;
  --ink:#8b9196;
  --ink-dark:#6f767c;
  --white:#ffffff;
  --photo-a:#8c7a6a;
  --photo-b:#a0604f;
  --photo-c:#8e8266;
}
*{margin:0;padding:0;box-sizing:border-box}
html,body{width:1200px;height:1159px;overflow:hidden;background:var(--white)}
body{font-family:"Source Sans 3",sans-serif;color:var(--ink);position:relative}
.abs{position:absolute}

.lang{left:971px;top:10px;font-weight:700;font-size:14px;color:var(--slate);letter-spacing:.5px}
.lang .on{color:var(--cyan)}
.brand{left:412px;top:30px;width:380px;height:80px;display:flex;align-items:center;gap:14px}
.brand-dot{width:80px;height:80px;border-radius:50%;background:var(--slate);flex:none}
.brand-text .name{font-size:36px;font-weight:600;color:var(--cyan);line-height:1}
.brand-text .tag{font-size:14px;color:var(--slate);margin-top:6px}

.nav{left:0;top:143px;width:1200px;height:76px;background:var(--slate)}
.nav ul{list-style:none;position:absolute;left:176px;top:0;display:flex;height:76px}
.nav li{width:141px;height:76px;display:flex;align-items:center;justify-content:center;
  color:var(--white);font-weight:700;font-size:14px;letter-spacing:.4px;border-right:1px solid var(--slate-line)}
.nav li:last-child{border-right:none}
.nav li.active{background:var(--cyan)}
.stripe{left:0;width:1200px;background:var(--cyan)}

.crumbs{left:0;top:233px;width:1200px;height:40px;background:var(--mist);
  display:flex;align-items:center;justify-content:center;font-size:13px;gap:14px}
.crumbs .here{color:var(--cyan)}

.team-figure{left:174px;top:297px;width:70px;height:88px;background:linear-gradient(#eef0f2,#dfe3e6);border-radius:30px 30px 6px 6px}
.title{left:272px;top:293px;font-size:39px;color:var(--cyan);letter-spacing:.5px;line-height:1.1}
.lead{left:272px;top:338px;font-size:20px;color:var(--ink-dark);line-height:26px;letter-spacing:.3px}
.copy{left:174px;width:880px;font-size:12.5px;line-height:16px}
.subhead{left:174px;top:599px;font-size:19px;color:var(--cyan);letter-spacing:.3px}

.gallery{left:0;top:721px;width:1200px;height:239px;background:var(--mist)}
.photo{top:41px;width:235px;height:158px}
.arrow{top:99px;width:30px;height:36px}

.footer{left:0;top:970px;width:1200px;height:189px;background:var(--slate);color:var(--white);font-size:12.5px}
.footer .col{position:absolute;top:25px;line-height:20.5px}
.footer .nav-col{font-weight:700;letter-spacing:.3px}
.follow{left:772px;top:24px;font-size:20px;letter-spacing:.5px}
.social{top:57px;width:46px;height:46px;border-radius:50%;background:var(--white)}
</style>
</head>
<body>

<div class="abs lang"><span class="on">DE</span> &nbsp;I&nbsp; EN</div>

<div class="abs brand">
  <div class="brand-dot"></div>
  <div class="brand-text">
    <div class="name">Lumo Staffing</div>
    <div class="tag">International Promotion &amp; HR services</div>
  </div>
</div>

<nav class="abs nav">
  <ul>
    <li>SERVICES</li><li>PERSONAL</li><li class="active">TEAM</li>
    <li>REFERENZEN</li><li>KONTAKT</li><li>IMPRESSUM</li>
  </ul>
</nav>
<div class="abs stripe" style="top:219px;height:14px"></div>

<div class="abs crumbs"><span>Services</span><span>&gt;</span><span class="here">Promotion</span></div>

<div class="abs team-figure" role="img" aria-label="Silhouette einer Personengruppe"></div>
<h1 class="abs title">PROMOTION - LOREM IPSUM</h1>
<p class="abs lead">LOREM IPSUM DOLOR SIT AMET, CONSETETUR SADIPSCING,<br>ELITR SED DIAM NONUMY EIRMOD TEMPOR ET DOLORE.</p>

<p class="abs copy" style="top:421px">Lorem ipsum dolor sit amet, consetetur sadipscing elitr, sed diam nonumy eirmod tempor invidunt ut labore et dolore magna aliquyam erat, sed diam voluptua. At vero eos et accusam et justo duo dolores et ea rebum. Stet clita kasd gubergren, no sea takimata sanctus est Lorem ipsum dolor sit amet. Lorem ipsum dolor sit amet, consetetur sadipscing elitr, sed diam nonumy eirmod tempor invidunt ut labore et dolore magna aliquyam erat, sed diam voluptua. At vero eos et accusam et justo duo dolores et ea rebum.</p>
<p class="abs copy" style="top:500px">Lorem ipsum dolor sit amet, consetetur sadipscing elitr, sed diam nonumy eirmod tempor invidunt ut labore et dolore magna aliquyam erat, sed diam voluptua. At vero eos et accusam et justo duo dolores et ea rebum. Stet clita kasd gubergren, no sea takimata sanctus est Lorem ipsum dolor sit amet dolor sit amet. Lorem ipsum dolor sit amet, consetetur sadipscing elitr, sedt, consetetur sadipscing elitr diam nonumy eirmod tempor invidunt ut labore et dolore magna aliquyam erat, sed diam voluptua. At vero eos et accusam et justo duo dolores et ea rebum.</p>

<h2 class="abs subhead">EIRMOD TEMPOR ET DOLORE.</h2>
<p class="abs copy" style="top:638px">At vero eos et accusam et justo duo dolores et ea rebum. Stet clita kasd gubergren, no sea takimata sanctus est Lorem ipsum dolor sit amet dolor sit amet. Lorem ipsum dolor sit amet, consetetur sadipscing elitr, sedt, consetetur sadipscing elitr diam nonumy eirmod tempor invidunt ut labore et dolore magna aliquyam erat, sed diam voluptua. At vero eos et accusam et justo duo dolores et ea rebum.</p>

<section class="abs gallery">
  <svg class="abs arrow" style="left:174px" viewBox="0 0 30 36"><path d="M26 2 L6 18 L26 34" fill="none" stroke="#7ecbd8" stroke-width="7"/></svg>
  <div class="abs photo" style="left:234px;background:linear-gradient(160deg,#9a6a55,var(--photo-a) 55%,#7f8586)" role="img" aria-label="Promoterin verteilt vor einem Café Proben an Passanten"></div>
  <div class="abs photo" style="left:496px;background:linear-gradient(160deg,#b04a5a,var(--photo-b) 50%,#c9a046)" role="img" aria-label="Zwei Promoterinnen an einem Aufsteller mit Luftballons im Markt"></div>
  <div class="abs photo" style="left:758px;background:linear-gradient(160deg,#c9b48a,var(--photo-c) 50%,#6a6255)" role="img" aria-label="Zwei Promoterinnen mit roten Schürzen im Eingangsbereich eines Geschäfts"></div>
  <svg class="abs arrow" style="left:1023px" viewBox="0 0 30 36"><path d="M4 2 L24 18 L4 34" fill="none" stroke="#7ecbd8" stroke-width="7"/></svg>
</section>
<div class="abs stripe" style="top:960px;height:10px"></div>

<footer class="abs footer">
  <div class="col" style="left:176px">
    <strong>Lumo Staffing</strong><br>Lindenhofweg 9<br>D-83101 Talheim<br><br>info@lumo-staffing.de<br>www.lumo-staffing.de
  </div>
  <div class="col nav-col" style="left:477px">SERVICES<br>PERSONAL<br>TEAM<br>REFERENZEN<br>KONTAKT<br>IMPRESSUM</div>
  <div class="abs follow">FOLGE UNS</div>
  <div class="abs social" style="left:772px" aria-label="Soziales Netzwerk 1"></div>
  <div class="abs social" style="left:829px" aria-label="Soziales Netzwerk 2"></div>
</footer>

</body>
</html>
```